Data Collection Workbook

We are creating a data gathering booklet that will be completed by our clients (ages 40-90). Due to the volume of information being collected, we are looking for a format that is both inviting to complete and aesthetically pleasing to the eye. The final product will be approximately 20-30 pages, divided into 13 sections. A table of contents, as well as two sample pages are attached.

```html
<!DOCTYPE html>
<html lang="en">
<head>
<meta charset="utf-8">
<title>Data Collection Workbook – Sample Spread</title>
<link href="https://fonts.googleapis.com/css2?family=Source+Sans+3:wght@400&display=swap" rel="stylesheet">
<style>
  :root {
    --navy: #075a88;
    --navy-deep: #0a4a73;
    --sky: #29aedb;
    --blue-mid: #1495c9;
    --blue-soft: #7cc3e2;
    --grey-soft: #dfe7ea;
    --grey-mid: #b9ccd3;
    --grid-line: #2d7fb1;
    --text: #3a3a3a;
    --page: #ffffff;
    --canvas: #ffffff;
  }
  * { box-sizing: border-box; margin: 0; padding: 0; }
  html, body {
    width: 1200px; height: 960px; overflow: hidden;
    background: var(--canvas);
  }
  .spread {
    position: absolute;
    left: 40px; top: 122px;
    width: 1120px; height: 716px;
    background: var(--page);
    font-family: "Source Sans 3", sans-serif;
    color: var(--text);
  }
  .spread-bands { position: absolute; inset: 0; }
  .text-block {
    position: absolute;
    width: 494px;
    font-size: 10.6px;
    line-height: 16px;
    text-align: justify;
  }
  .text-block p + p { margin-top: 14px; }
  .text-block p.gap { margin-top: 30px; }
  .page-left .text-block { left: 33px; top: 128px; }
  .page-right .text-block { left: 593px; top: 301px; }
  .data-grid {
    position: absolute;
    left: 683px; top: 69px;
    width: 316px; height: 203px;
    border-collapse: collapse;
  }
  .data-grid td { border: 1px solid var(--grid-line); }
  .pie-charts {
    position: absolute;
    left: 80px; top: 480px;
  }
</style>
</head>
<body>
<div class="spread">
  <svg class="spread-bands" width="1120" height="716" viewBox="0 0 1120 716">
    <polygon points="0,0 0,87 560,45 560,0" fill="var(--sky)"/>
    <polygon points="0,0 1120,0 560,45" fill="var(--navy)"/>
    <polygon points="0,716 560,670 1120,716" fill="var(--navy)"/>
    <polygon points="560,670 1120,629 1120,716" fill="var(--sky)"/>
    <line x1="560.5" y1="45" x2="560.5" y2="670" stroke="var(--grid-line)" stroke-width="1"/>
  </svg>

  <section class="page-left">
    <div class="text-block">
      <p>Lorem Ipsum is simply dummy text of the printing and typesetting industry. Lorem Ipsum has been the industry's standard dummy text ever since the 1500s, when an unknown printer took a galley of type and scrambled it to make a type specimen book. It has survived not only five centuries, but also the leap into electronic typesetting, remaining essentially unchanged. It was popularised in the 1960s with the release of Graphline sheets containing Lorem Ipsum passages, and more recently with desktop publishing software like Folio Layout including versions of Lorem Ipsum.</p>
      <p>It is a long established fact that a reader will be distracted by the readable content of a page when looking at its layout. The point of using Lorem Ipsum is that it has a more-or-less normal distribution of letters, as opposed to using 'Content here, content here', making it look like readable English. Many desktop publishing packages and web page editors now use Lorem Ipsum as their default model text, and a search for 'lorem ipsum' will uncover many web sites still in their infancy. Various versions have evolved over the years, sometimes by accident, sometimes on purpose (injected humour and the like).</p>
      <p class="gap">Contrary to popular belief, Lorem Ipsum is not simply random text. It has roots in a piece of classical Latin literature from 45 BC, making it over 2000 years old. Daniel Harrow, a Latin professor at Linwood College in Vermont, looked up one of the more obscure Latin words, consectetur, from a Lorem Ipsum passage, and going through the cites of the word in classical literature, disco vered the undoubtable source. Lorem Ipsum</p>
    </div>

    <svg class="pie-charts" width="400" height="200" viewBox="0 0 400 200" role="img" aria-label="Two pie charts">
      <defs>
        <path id="wedge30" d="M0,0 L0,-1 A1 1 0 0 1 0.5,-0.866 Z"/>
      </defs>
      <g class="pie-exploded" transform="translate(95,113)">
        <use href="#wedge30" transform="rotate(0) scale(70)" fill="var(--blue-soft)"/>
        <use href="#wedge30" transform="rotate(30) translate(8,-12) scale(66)" fill="var(--sky)"/>
        <use href="#wedge30" transform="rotate(60) scale(72)" fill="var(--blue-mid)"/>
        <use href="#wedge30" transform="rotate(90) scale(70)" fill="#0e86bf"/>
        <use href="#wedge30" transform="rotate(120) scale(74)" fill="#0f6fa5"/>
        <use href="#wedge30" transform="rotate(150) scale(74)" fill="var(--navy)"/>
        <use href="#wedge30" transform="rotate(180) scale(72)" fill="var(--navy-deep)"/>
        <use href="#wedge30" transform="rotate(210) scale(70)" fill="#15a6d8"/>
        <use href="#wedge30" transform="rotate(240) scale(66)" fill="#aac6cf"/>
        <use href="#wedge30" transform="rotate(270) scale(68)" fill="var(--grey-mid)"/>
        <use href="#wedge30" transform="rotate(300) scale(64)" fill="var(--grey-soft)"/>
        <use href="#wedge30" transform="rotate(330) translate(-2,-10) scale(72)" fill="#a9d5ea"/>
      </g>
      <g class="pie-solid" transform="translate(292,93)">
        <path d="M0,0 L0,-82 A82 82 0 0 1 47,-67.2 Z" fill="var(--blue-soft)"/>
        <path d="M0,0 L47,-67.2 A82 82 0 0 1 77.1,-28 Z" fill="var(--sky)"/>
        <path d="M0,0 L77.1,-28 A82 82 0 0 1 80.8,14.2 Z" fill="var(--blue-mid)"/>
        <path d="M0,0 L80.8,14.2 A82 82 0 0 1 67.2,47 Z" fill="#0e86bf"/>
        <path d="M0,10 L67.2,57 A82 82 0 0 1 -67.2,57 Z" fill="var(--grey-soft)"/>
        <path d="M0,0 L-67.2,47 A82 82 0 0 1 0,-82 Z" fill="var(--navy-deep)"/>
      </g>
    </svg>
  </section>

  <section class="page-right">
    <table class="data-grid" aria-label="Blank entry grid">
      <tbody>
        <tr><td></td><td></td><td></td><td></td><td></td><td></td><td></td><td></td><td></td><td></td><td></td></tr>
        <tr><td></td><td></td><td></td><td></td><td></td><td></td><td></td><td></td><td></td><td></td><td></td></tr>
        <tr><td></td><td></td><td></td><td></td><td></td><td></td><td></td><td></td><td></td><td></td><td></td></tr>
        <tr><td></td><td></td><td></td><td></td><td></td><td></td><td></td><td></td><td></td><td></td><td></td></tr>
        <tr><td></td><td></td><td></td><td></td><td></td><td></td><td></td><td></td><td></td><td></td><td></td></tr>
        <tr><td></td><td></td><td></td><td></td><td></td><td></td><td></td><td></td><td></td><td></td><td></td></tr>
        <tr><td></td><td></td><td></td><td></td><td></td><td></td><td></td><td></td><td></td><td></td><td></td></tr>
        <tr><td></td><td></td><td></td><td></td><td></td><td></td><td></td><td></td><td></td><td></td><td></td></tr>
        <tr><td></td><td></td><td></td><td></td><td></td><td></td><td></td><td></td><td></td><td></td><td></td></tr>
        <tr><td></td><td></td><td></td><td></td><td></td><td></td><td></td><td></td><td></td><td></td><td></td></tr>
        <tr><td></td><td></td><td></td><td></td><td></td><td></td><td></td><td></td><td></td><td></td><td></td></tr>
      </tbody>
    </table>

    <div class="text-block">
      <p>Lorem Ipsum is simply dummy text of the printing and typesetting industry. Lorem Ipsum has been the industry's standard dummy text ever since the 1500s, when an unknown printer took a galley of type and scrambled it to make a type specimen book. It has survived not only five centuries, but also the leap into electronic typesetting, remaining essentially unchanged. It was popularised in the 1960s with the release of Graphline sheets containing Lorem Ipsum passages, and more recently with desktop publishing software like Folio Layout including versions of Lorem Ipsum.</p>
      <p>It is a long established fact that a reader will be distracted by the readable content of a page when looking at its layout. The point of using Lorem Ipsum is that it has a more-or-less normal distribution of letters, as opposed to using 'Content here, content here', making it look like readable English. Many desktop publishing packages and web page editors now use Lorem Ipsum as their default model text, and a search for 'lorem ipsum' will uncover many web sites still in their infancy. Various versions have evolved over the years, sometimes by accident, sometimes on purpose (injected humour and the like).</p>
      <p class="gap">Contrary to popular belief, Lorem Ipsum is not simply random text. It has roots in a piece of classical Latin literature from 45 BC, making it over 2000 years old. Daniel Harrow, a Latin professor at Linwood College in Vermont, looked up one of the more obscure Latin words, consectetur, from a Lorem Ipsum passage, and going through the cites of the word in classical literature, disco vered the undoubtable source. Lorem Ipsum</p>
    </div>
  </section>
</div>
</body>
</html>
```